Racing Simulator Website

We're a new startup designing, selling, and supporting racing simulators, specifically targeted at Track Day enthusiasts and Club Racers alike. We are differentiating ourselves from other Racing Simulator companies by fully supporting the software and hardware of our systems. The client does not need to update their software to keep the simulator running, and any issues they may run into with the hardware, we will fix. We've designed our systems with this in mind and have added features that make it as easy for the client to operate as possible. Our current website says this but doesn't do a good job of highlighting how much easier these extra features make the simulator to live with.

Our systems look like a single console in the sense that the user neither sees nor interacts with the computer underneath but just uses the simulator using a simple button box. Our computers are connected to our cloud to keep Windows, the device drivers, and all the supported simulation games up to date, so that the system is always ready to use. Furthermore, we offer our systems as "lease-to-own" with small down payment and monthly installments, which also cover the ongoing hardware and software support for the duration of the lease. All other turnkey racing simulators require the full amount to be paid up front and do not offer software support to keep the systems up to date or provide anything beyond warranty service on the hardware.

We already have a website that contains most of this information, but it is not exciting. We're engineers building the systems but frankly do not know how to make our website exciting and compelling. We want the Home page experience to be much richer and ideally carry all these points across.

As we target track-day enthusiasts and club racers, we are positioning our simulators as tools to improve your technique and reflexes to improve your driving on the real track.
Our current website is here https://www.bluefernmotion.com
We already have more photos than what is currently on the website that you can use, or feel free to request specific photos of the system.

```html
<!DOCTYPE html>
<html lang="en">
<head>
<meta charset="utf-8">
<title>Bluefern Motion – Racing Simulators</title>
<link href="https://fonts.googleapis.com/css2?family=Lato:wght@400;700;900&family=Montserrat:wght@600;700;800&display=swap" rel="stylesheet">
<style>
:root{
  --navy:#1b3558;
  --navy-dark:#13294b;
  --yellow:#f8b62e;
  --ice:#e0f0fb;
  --text:#3c4654;
  --white:#ffffff;
  --line:#d9dee5;
}
*{box-sizing:border-box;margin:0;padding:0}
html,body{width:1200px;height:3735px;overflow:hidden;background:var(--white)}
body{font-family:'Lato',sans-serif;color:var(--text);position:relative}
.abs{position:absolute}
.heading{font-family:'Montserrat',sans-serif;font-weight:700;color:var(--navy);font-size:40px;line-height:1.1}
.heading .accent{color:var(--yellow);font-weight:800}
.rule{position:absolute;height:3px;background:var(--navy)}
.btn{position:absolute;background:var(--yellow);color:var(--white);font-weight:700;font-size:17px;display:flex;align-items:center;justify-content:center}
.para{font-size:15px;line-height:25.6px;text-align:justify;color:var(--text)}
.ph{position:absolute}

/* top bar */
.topbar{position:absolute;left:0;top:0;width:1200px;height:35px;background:var(--navy-dark);color:var(--white);font-size:15px}
.topbar .phone{position:absolute;left:112px;top:8px;display:flex;align-items:center;gap:6px}
.topbar .login{position:absolute;left:1000px;top:7px;font-weight:700}
.topbar .sep{position:absolute;left:1052px;top:7px;width:1px;height:21px;background:#fff}
/* header */
.header{position:absolute;left:0;top:35px;width:1200px;height:91px;background:var(--white)}
.brand{position:absolute;display:flex;align-items:center;gap:10px;font-family:'Lato',sans-serif;font-weight:900;color:var(--navy)}
.brand .mark{width:18px;height:18px;background:var(--yellow)}
.nav{position:absolute;top:30px;left:370px;display:flex;gap:27px;font-size:15px;color:#333}
.contact-btn{left:942px;top:18px;width:146px;height:48px;font-weight:400;font-size:18px}
/* hero */
.hero{position:absolute;left:0;top:126px;width:1200px;height:529px;background:radial-gradient(ellipse at 50% 35%,#3a4652 0%,#1a2028 55%,#0b0e12 100%)}
.hero h1{position:absolute;left:0;width:1200px;top:158px;text-align:center;font-family:'Montserrat',sans-serif;font-weight:700;font-size:54px;line-height:64px;color:var(--white)}
.hero p{position:absolute;left:0;width:1200px;top:302px;text-align:center;font-size:17px;line-height:27px;font-weight:700;color:var(--white)}
.hero .btn{left:506px;top:380px;width:185px;height:43px}
.play{position:absolute;left:580px;top:448px;width:40px;height:40px;border-radius:50%;background:#5a5f66}
/* about */
.about-frame{left:120px;top:752px;width:412px;height:414px;background:var(--yellow)}
.about-img{left:112px;top:742px;width:411px;height:414px;background:linear-gradient(160deg,#c9c9c9,#6b6b6b 60%,#2a2a2a)}
/* what we do */
.wwd{position:absolute;left:0;top:1253px;width:1200px;height:603px;background:var(--ice)}
.card{position:absolute;top:174px;width:308px;height:344px;background:var(--white);border:1px solid var(--line)}
.card .img{position:absolute;left:8px;top:8px;width:292px;height:252px}
.card .title{position:absolute;left:0;top:268px;width:100%;text-align:center;font-size:21px;line-height:29px;color:#222}
/* sim racing */
.sim-frame{left:652px;top:1952px;width:436px;height:407px;background:var(--navy)}
.sim-img{left:640px;top:1943px;width:440px;height:407px;background:linear-gradient(180deg,#2d3b4c 0%,#1b2530 50%,#5a2418 75%,#141a22 100%)}
/* cta */
.cta{position:absolute;left:0;top:2460px;width:1200px;height:358px;background:linear-gradient(90deg,#1c3556 0%,#213c61 50%,#1a3150 100%)}
.cta .heading{position:absolute;left:0;width:1200px;top:80px;text-align:center;color:var(--white)}
.cta p{position:absolute;left:0;width:1200px;top:172px;text-align:center;color:var(--white);font-weight:700;font-size:17px}
.cta .btn{left:519px;top:225px;width:161px;height:46px}
/* testimonials */
.tcard{position:absolute;top:3002px;width:310px;height:236px;background:var(--white);border:1px solid #e3e6ea;box-shadow:0 2px 8px rgba(0,0,0,.08);border-radius:4px}
.tcard .q{position:absolute;left:22px;top:12px}
.tcard .lead{position:absolute;left:24px;top:40px;font-size:17px;color:#222}
.tcard .body{position:absolute;left:24px;top:72px;width:270px;font-size:13.5px;line-height:25px;color:#444}
.tcard .avatar{position:absolute;left:22px;top:150px;width:70px;height:70px;border-radius:50%;background:linear-gradient(180deg,#d9dde2,#9aa3ad)}
.tcard .name{position:absolute;left:114px;top:162px;font-size:19px;color:#222}
.tcard .role{position:absolute;left:114px;top:193px;font-size:14px;color:#555}
/* footer */
.footer{position:absolute;left:0;top:3325px;width:1200px;height:410px;background:var(--navy)}
.footer h4{position:absolute;top:102px;font-size:20px;font-weight:700;color:var(--white)}
.footer .frule{position:absolute;top:136px;height:2px;width:80px;background:var(--white)}
.footer ul{position:absolute;top:140px;list-style:none;color:var(--white);font-size:15px}
.footer li{height:34px;display:flex;align-items:center;gap:14px}
.footer li::before{content:"";width:7px;height:7px;border-radius:50%;background:var(--white)}
.footer .email{position:absolute;left:112px;top:187px;width:218px;height:42px;background:var(--white);font-size:15px;color:#555;padding:12px 22px}
.footer .btn{left:112px;top:239px;width:117px;height:42px;font-size:17px}
.contact-line{position:absolute;left:882px;display:flex;gap:10px;color:var(--white);font-size:15px;line-height:24px}
.footer .divider{position:absolute;left:112px;top:357px;width:976px;height:1px;background:#6b7f99}
.social{position:absolute;top:368px;width:22px;height:22px;border-radius:50%;background:var(--white)}
</style>
</head>
<body>

<div class="topbar">
  <div class="phone">
    <svg width="16" height="16" viewBox="0 0 24 24"><path d="M6.6 10.8a15 15 0 0 0 6.6 6.6l2.2-2.2c.3-.3.7-.4 1-.2 1.1.4 2.3.6 3.6.6.6 0 1 .4 1 1V20c0 .6-.4 1-1 1C10.6 21 3 13.4 3 4c0-.6.4-1 1-1h3.5c.6 0 1 .4 1 1 0 1.3.2 2.5.6 3.6.1.3 0 .7-.2 1z" fill="#f8b62e"/></svg>
    +1 555 014 2290
  </div>
  <div class="login">Login</div>
  <div class="sep"></div>
  <svg class="abs" style="left:1070px;top:6px" width="20" height="22" viewBox="0 0 20 22"><path d="M6 7V5a4 4 0 0 1 8 0v2" stroke="#f8b62e" stroke-width="2" fill="none"/><rect x="2" y="7" width="16" height="14" rx="2" fill="#f8b62e"/></svg>
</div>

<header class="header">
  <div class="brand" style="left:68px;top:30px;font-size:28px"><span class="mark"></span>Bluefern Motion</div>
  <nav class="nav">
    <span>Home</span><span>About</span><span>What We Do</span><span>What is Sim Racing</span><span>Models</span><span>Coaching</span>
  </nav>
  <div class="btn contact-btn">Contact Us</div>
</header>

<section class="hero" role="img" aria-label="Dark studio with a triple-screen racing simulator rig">
  <h1>Drive. Train. Compete.<br>We’ll handle the rest.</h1>
  <p>Professional-grade racing simulators built for real drivers — always<br>updated, fully supported, and ready to race.</p>
  <div class="btn">Get My Simulator</div>
  <div class="play"><svg width="40" height="40" viewBox="0 0 40 40"><path d="M16 13l11 7-11 7z" fill="#fff"/></svg></div>
</section>

<section class="about">
  <div class="ph about-frame"></div>
  <div class="ph about-img" role="img" aria-label="Simulator rig with curved monitor, steering wheel and racing seat"></div>
  <h2 class="heading abs" style="left:642px;top:772px"><span class="accent">About</span> Bluefern Motion</h2>
  <div class="rule" style="left:642px;top:830px;width:150px"></div>
  <p class="para abs" style="left:642px;top:855px;width:448px">Want to practice your driving and race craft without risking your safety or wallet? Racing simulators allow you to practice virtually any track in whatever car you want with zero risk. Bluefern Motion is here to get you started on your sim racing journey. From building and installing your custom simulator to tech support and driver coaching, Bluefern Motion is just a call or email away.</p>
  <div class="btn" style="left:642px;top:1059px;width:146px;height:46px">Read More</div>
</section>

<section class="wwd">
  <h2 class="heading abs" style="left:0;width:1200px;text-align:center;top:76px"><span class="accent">What</span> We Do</h2>
  <div class="rule" style="left:523px;top:135px;width:150px"></div>
  <div class="card" style="left:112px">
    <div class="img" role="img" aria-label="Cockpit view of a simulator with wheel and track on screens" style="background:linear-gradient(180deg,#8fb0d2 0%,#6f8d6a 40%,#2a2a2a 60%,#1a1a1a 100%)"></div>
    <div class="title">Bringing Pro-Level Racing<br>Simulation to Everyone</div>
  </div>
  <div class="card" style="left:445px">
    <div class="img" role="img" aria-label="Shifter and button box on a simulator rig" style="background:linear-gradient(160deg,#3a3a3a,#121212)"></div>
    <div class="title">The Problem with Traditional<br>Turnkey Simulators</div>
  </div>
  <div class="card" style="left:780px">
    <div class="img" role="img" aria-label="Compact simulator chassis with seat and pedals" style="background:linear-gradient(160deg,#d8d8d8,#7b7b7b 60%,#3a3a3a)"></div>
    <div class="title">Designed for Convenience &amp;<br>Performance</div>
  </div>
</section>

<section class="sim">
  <h2 class="heading abs" style="left:112px;top:1934px"><span class="accent">What</span> is Sim Racing?</h2>
  <div class="rule" style="left:112px;top:1993px;width:150px"></div>
  <p class="para abs" style="left:112px;top:2024px;width:446px">Racing simulators have been around for quite some time. While their ability to simulate the driving experience has dramatically improved since they first appeared, the main components are basically the same. There are controllers that look and feel like controls in a car; pedals, a steering wheel, a shifter and maybe some more buttons that would control certain aspects such as traction control, etc. All these controls are arranged in a chassis, with a driver’s seat, speakers and monitor(s) completing the experience of a car. What makes all this work is a powerful computer that runs some simulation software. While this software is sometimes referred to as a game, it is indeed a very sophisticated simulation</p>
  <div class="btn" style="left:112px;top:2327px;width:146px;height:46px">Read More</div>
  <div class="ph sim-frame"></div>
  <div class="ph sim-img" role="img" aria-label="Triple-monitor sim racing desk lit with red accent lights"></div>
</section>

<section class="cta" role="img" aria-label="Dimmed view of a simulator cockpit behind a navy overlay">
  <h2 class="heading"><span class="accent">Ready to</span> Race Smarter?</h2>
  <div class="rule" style="left:523px;top:137px;width:150px;background:#fff"></div>
  <p>Get a personalized simulator recommendation and start your journey today.</p>
  <div class="btn">Get My Quote</div>
</section>

<section class="testimonials">
  <h2 class="heading abs" style="left:0;width:1200px;text-align:center;top:2893px"><span class="accent">What</span> Real Drivers Are Saying</h2>
  <div class="rule" style="left:523px;top:2952px;width:150px"></div>

  <div class="tcard" style="left:112px">
    <svg class="q" width="40" height="28" viewBox="0 0 40 28"><path d="M2 26V16C2 8 6 3 14 2v5c-4 1-6 4-6 8h6v11zM22 26V16c0-8 4-13 12-14v5c-4 1-6 4-6 8h6v11z" fill="#8795a6"/></svg>
    <div class="lead">I just turn it on and drive.</div>
    <div class="body">I’ve used other simulators before, and I always spent more time updating software than actually driving. With my</div>
    <div class="avatar" role="img" aria-label="Customer portrait"></div>
    <div class="name">Dale Whitford,</div>
    <div class="role">Regional Club Racer</div>
  </div>
  <div class="tcard" style="left:447px">
    <svg class="q" width="40" height="28" viewBox="0 0 40 28"><path d="M2 26V16C2 8 6 3 14 2v5c-4 1-6 4-6 8h6v11zM22 26V16c0-8 4-13 12-14v5c-4 1-6 4-6 8h6v11z" fill="#8795a6"/></svg>
    <div class="lead">It feels like my real car on track.</div>
    <div class="body">The feedback and setup are spot on, and the support team has helped me fine-tune everything to match my actual race car.</div>
    <div class="avatar" role="img" aria-label="Customer portrait"></div>
    <div class="name">Kevin Marsh,</div>
    <div class="role">Track-Day Enthusiast</div>
  </div>
  <div class="tcard" style="left:782px">
    <svg class="q" width="40" height="28" viewBox="0 0 40 28"><path d="M2 26V16C2 8 6 3 14 2v5c-4 1-6 4-6 8h6v11zM22 26V16c0-8 4-13 12-14v5c-4 1-6 4-6 8h6v11z" fill="#8795a6"/></svg>
    <div class="lead">Support that understands racing.</div>
    <div class="body">I had one small hardware issue — they handled it remotely within a day. I’ve never experienced that kind of follow-up</div>
    <div class="avatar" role="img" aria-label="Customer portrait"></div>
    <div class="name">Lena Ortiz,</div>
    <div class="role">HPDE Program Driver</div>
  </div>
</section>

<footer class="footer">
  <div class="brand" style="left:112px;top:98px;font-size:28px;color:var(--white)"><span class="mark"></span>Bluefern Motion</div>
  <div class="email">Email</div>
  <div class="btn">Subscribe</div>

  <h4 style="left:430px">Quick Links</h4><div class="frule" style="left:430px"></div>
  <ul style="left:432px"><li>Home</li><li>About</li><li>What We Do</li><li>What is Sim Racing</li><li>Models</li><li>Coaching</li></ul>

  <h4 style="left:646px">Help Links</h4><div class="frule" style="left:646px"></div>
  <ul style="left:648px"><li>Privacy Policy</li><li>Terms &amp; Conditions</li><li>Cookies</li></ul>

  <h4 style="left:882px">Contact Us</h4><div class="frule" style="left:882px"></div>
  <div class="contact-line" style="top:152px">
    <svg width="18" height="18" viewBox="0 0 24 24" style="margin-top:3px"><circle cx="12" cy="12" r="11" fill="#fff"/><path d="M12 5a4.5 4.5 0 0 0-4.5 4.5c0 3.3 4.5 8.5 4.5 8.5s4.5-5.2 4.5-8.5A4.5 4.5 0 0 0 12 5zm0 6a1.5 1.5 0 1 1 0-3 1.5 1.5 0 0 1 0 3z" fill="#1b3558"/></svg>
    <span>220 Alder Lane,<br>Portland, OR 97205</span>
  </div>
  <div class="contact-line" style="top:218px">
    <svg width="18" height="18" viewBox="0 0 24 24" style="margin-top:3px"><circle cx="12" cy="12" r="11" fill="#fff"/><rect x="6" y="8" width="12" height="8" fill="#1b3558"/><path d="M6 8l6 5 6-5" stroke="#fff" stroke-width="1.2" fill="none"/></svg>
    <span>hello@bluefernmotion.com</span>
  </div>
  <div class="contact-line" style="top:264px">
    <svg width="18" height="18" viewBox="0 0 24 24" style="margin-top:3px"><circle cx="12" cy="12" r="11" fill="#fff"/><path d="M9 7l2 3-1.3 1.3a7 7 0 0 0 3 3L14 13l3 2-1 2c-4 0-8-4-8-8z" fill="#1b3558"/></svg>
    <span>+1 555 014 2290</span>
  </div>

  <div class="divider"></div>
  <div class="social" style="left:112px"></div>
  <div class="social" style="left:148px"></div>
</footer>

</body>
</html>
```